Business Card Design Project

parking lot sealing and striping company

Industry/Entity Type

Business

Contact Information for Business Card

See pics below, blue and gray colors

```html
<!DOCTYPE html>
<html lang="en">
<head>
<meta charset="utf-8">
<title>Tarline Pavement – Business Card</title>
<link href="https://fonts.googleapis.com/css2?family=Montserrat:wght@400;500;700;800&family=Open+Sans:ital,wght@1,700&family=Oswald:wght@400&display=swap" rel="stylesheet">
<style>
  :root{
    --bg:#d4d4d6;
    --card:#f6f5f8;
    --ink:#1c1c1c;
    --black:#1b1b1b;
    --yellow:#f2c200;
    --blue:#1aa3e0;
    --royal:#1f3fd6;
    --white:#ffffff;
    --label:#222222;
  }
  *{margin:0;padding:0;box-sizing:border-box}
  html,body{width:1200px;height:941px;overflow:hidden;background:var(--bg)}
  body{position:relative;font-family:"Montserrat",sans-serif;color:var(--ink)}

  .side-label{
    position:absolute;font-family:"Open Sans",sans-serif;font-style:italic;font-weight:700;
    font-size:19px;letter-spacing:3px;line-height:1.3;color:var(--label)
  }
  .side-label--back{left:760px;top:96px}
  .side-label--front{left:760px;top:420px}

  .card{
    position:absolute;width:580px;height:331px;background:var(--card);overflow:hidden;
    box-shadow:0 14px 30px rgba(0,0,0,.18)
  }
  .card--back{left:70px;top:90px}
  .card--front{left:560px;top:520px}

  .brand{display:flex;align-items:center;gap:12px}
  .brand__mark{width:44px;height:44px;background:var(--black)}
  .brand__name{font-weight:800;font-size:26px;line-height:1.05;letter-spacing:1px;color:var(--ink)}
  .brand__name span{display:block;font-size:13px;letter-spacing:4px}

  .card--back .brand{position:absolute;left:170px;top:92px}
  .address-band{position:absolute;left:0;right:0;bottom:0;height:100px}
  .address-band__blue{height:10px;background:var(--blue)}
  .address-band__yellow{height:90px;background:var(--yellow);display:flex;align-items:center;justify-content:center}
  .address-band__text{font-size:11px;font-weight:500;letter-spacing:.6px;color:var(--ink)}

  .front-art{position:absolute;inset:0}
  .card--front .brand{position:absolute;right:34px;top:46px}
  .card--front .brand__mark{width:40px;height:40px}
  .card--front .brand__name{font-size:23px}
  .card--front .brand__name span{font-size:12px;letter-spacing:3.4px}

  .contact{position:absolute;right:30px;top:140px;text-align:right}
  .contact__name{font-weight:800;font-size:17px;letter-spacing:.5px;margin-bottom:10px}
  .contact__row{display:flex;justify-content:flex-end;align-items:center;gap:7px;font-size:12px;line-height:19px}
  .contact__row svg{width:11px;height:11px;fill:var(--ink)}

  .services{position:absolute;left:24px;top:128px;list-style:none}
  .services li{
    display:flex;align-items:center;gap:8px;font-family:"Oswald",sans-serif;font-size:12.5px;
    letter-spacing:.6px;line-height:19px;color:var(--white);text-transform:uppercase
  }
  .services li::before{content:"";width:7px;height:7px;border:1.5px solid var(--white);border-radius:50%}
</style>
</head>
<body>

<div class="side-label side-label--back">BACK SIDE<br>CMYK MODE</div>
<div class="side-label side-label--front">FRONT SIDE<br>CMYK MODE</div>

<section class="card card--back">
  <div class="brand">
    <div class="brand__mark"></div>
    <div class="brand__name">TARLINE<span>PAVEMENT</span></div>
  </div>
  <div class="address-band">
    <div class="address-band__blue"></div>
    <div class="address-band__yellow">
      <p class="address-band__text">DUMMY OFFICE ADDRESS, STREET NAME, LOCATION, STREET, STATE, COUNTRY</p>
    </div>
  </div>
</section>

<section class="card card--front">
  <svg class="front-art" viewBox="0 0 580 331" width="580" height="331">
    <polygon points="0,0 412,331 0,331" fill="var(--royal)"/>
    <polygon points="0,0 400,331 0,331" fill="var(--yellow)"/>
    <polygon points="0,0 388,331 0,331" fill="var(--black)"/>
  </svg>

  <div class="brand">
    <div class="brand__mark"></div>
    <div class="brand__name">TARLINE<span>PAVEMENT</span></div>
  </div>

  <div class="contact">
    <p class="contact__name">DALE PORTER</p>
    <p class="contact__row">91 40215 73064
      <svg viewBox="0 0 24 24"><path d="M6.6 10.8a15.1 15.1 0 0 0 6.6 6.6l2.2-2.2c.3-.3.7-.4 1-.2 1.1.4 2.3.6 3.6.6.6 0 1 .4 1 1V20c0 .6-.4 1-1 1A17 17 0 0 1 3 4c0-.6.4-1 1-1h3.5c.6 0 1 .4 1 1 0 1.3.2 2.5.6 3.6.1.3 0 .7-.2 1z"/></svg>
    </p>
    <p class="contact__row">info@tarlinepave.com
      <svg viewBox="0 0 24 24"><path d="M2 5h20v14H2zm2 2v.5l8 5 8-5V7l-8 5z"/></svg>
    </p>
    <p class="contact__row">www.tarlinepave.com
      <svg viewBox="0 0 24 24"><path d="M12 2a10 10 0 1 0 0 20 10 10 0 0 0 0-20zm0 2.2A7.8 7.8 0 0 1 19.8 12H4.2A7.8 7.8 0 0 1 12 4.2zM4.3 13.5h15.4a7.8 7.8 0 0 1-15.4 0z"/></svg>
    </p>
  </div>

  <ul class="services">
    <li>Asphalt Sealing</li>
    <li>Crack Repair</li>
    <li>Ramp Building</li>
    <li>Line Painting</li>
    <li>Concrete Curb</li>
    <li>Walkway Sealing</li>
    <li>Oil Stain Removal</li>
    <li>Parking Lot Cleaning Up</li>
    <li>Pothole and Gap Filling</li>
  </ul>
</section>

</body>
</html>
```